Fjellbrook Botanics - Black Face Mask Packaging Design

We require packaging design for a charcoal activated blackhead removal peel off face mask (please see attachment of competitors product).

1: We require a logo for our brand name: 'Fjellbrook Botanics'

2: We require a 3d rendered image of the box with the tube

3: We require label templates for both the box and the tube

The logo design brief is as follows:

We are bringing out a range of natural beauty products. We require a logo that represents norwegian natural beauty & incorporates the Norwegian Flag.

The packaging design brief is as follows:

Please attachment: (FBGen). There is an image of a woman with a black face mask.

1:We require our packaging design to have a generic face with a face mask being pulled off/stretched (as shown in the above attachment).
However, the face mask should display a Norwegian flag. The part of the mask that is still fixed to the face should be in full pastel Norwegian flag colors. The part of the mask that has been peeled away should be faded to charcoal grey (whilst maintaining the Norwegian flag). The ratio should be around 50/50 of mask attached to mask being peeled.
The colors throughout should be soft.

2:The design should also incorporate a unisex logo.(Please see attachment: FBUnisex)

3: The design should display the wording: 'Charcoal Activated Face Mask'

4: The design should also display the tagline: 'restores your youthful glow'

5: The back of the tube should display the ingredients: Please see attached. The back should also say ISO901 & GMPC certified

Please note, the packaging design for the tube should just be black and white as the printing machine on the tube can only be white.

The box can be a variation of colors as there are no restrictions on the colors for printing onto cardboard

Target Market(s)

Beauty, Natural Beauty, Unisex

Industry/Entity Type

Product

Logo Text

Fjellbrook Botanics

Requirements
Must have
• Please refer to project description
Nice to have

```html
<!DOCTYPE html>
<html lang="en">
<head>
<meta charset="utf-8">
<title>Fjellbrook Botanics – Charcoal Activated Face Mask Box Dieline</title>
<link rel="stylesheet" href="https://fonts.googleapis.com/css2?family=Libre+Bodoni:wght@400&family=Josefin+Sans:wght@300&display=swap">
<style>
  :root {
    --backdrop: #4d4d4d;
    --board: #ffffff;
    --ink: #000000;
    --fold: #bdbdbd;
    --muted: #9a9a9a;
    --faint: #c8c8c8;
    --blush: #e79aa8;
    --swoosh-red: #e8a0ab;
    --swoosh-blue: #9fb3d9;
    --serif: "Libre Bodoni", "Bodoni Moda", serif;
    --sans: "Josefin Sans", sans-serif;
  }
  html, body { margin: 0; padding: 0; overflow: hidden; }
  body { width: 1158px; height: 1200px; background: var(--backdrop); }
  .dieline { position: relative; width: 1158px; height: 1200px; overflow: hidden; }
  .dieline-shapes { position: absolute; inset: 0; }
  .label { position: absolute; margin: 0; font-family: var(--serif); }

  .flap-name { left: 0; width: 280px; top: 162px; text-align: center; color: var(--board); font-size: 18px; letter-spacing: .5px; }
  .brand-name { left: 29px; top: 511px; color: var(--board); font-size: 46px; line-height: 48px; letter-spacing: -.5px; }
  .product-name { left: 52px; top: 628px; color: var(--ink); font-size: 20px; line-height: 27px; }
  .glow-swoosh {
    position: absolute; left: 19px; top: 672px; width: 252px; height: 86px; border-radius: 50%;
    background: radial-gradient(ellipse at 55% 55%, rgba(232,160,171,.55) 0%, rgba(159,179,217,.35) 40%, rgba(255,255,255,0) 72%);
  }
  .tagline { left: 0; width: 280px; top: 712px; text-align: center; color: var(--blush); font-size: 10px; }
  .volume { left: 0; width: 280px; top: 768px; text-align: center; color: var(--muted); font-family: var(--sans); font-size: 17px; letter-spacing: 1px; }

  .back-mark { left: 548px; width: 276px; top: 458px; text-align: center; color: var(--faint); font-size: 14px; }
  .ingredients { left: 630px; width: 130px; top: 618px; text-align: center; color: #333; font-size: 7px; line-height: 11px; text-transform: uppercase; }
  .certification { left: 548px; width: 276px; top: 705px; text-align: center; color: #333; font-size: 8px; letter-spacing: .3px; }
  .unisex-mark { left: 548px; width: 276px; top: 762px; text-align: center; color: var(--ink); font-size: 9px; }

  .front-mark { left: 826px; width: 282px; top: 540px; text-align: center; color: var(--ink); font-size: 24px; line-height: 28px; }
</style>
</head>
<body>
<main class="dieline">
  <svg class="dieline-shapes" width="1158" height="1200" viewBox="0 0 600 622" preserveAspectRatio="none" aria-hidden="true">
    <!-- side panel top flap -->
    <path d="M0,160 V12 Q0,0 12,0 H133 Q145,0 145,12 V160 Z" fill="#000"/>
    <line x1="0" y1="22" x2="145" y2="22" stroke="#555" stroke-width=".6"/>
    <!-- tuck tabs top -->
    <path d="M145,160 L162,112 Q168,97 185,97 H243 Q260,97 266,112 L283,160 Z" fill="#000"/>
    <path d="M428,160 L445,112 Q451,97 468,97 H534 Q551,97 557,112 L574,160 Z" fill="#000"/>
    <!-- body panels -->
    <rect x="0" y="160" width="600" height="295" fill="#fff"/>
    <rect x="0" y="265" width="283" height="55" fill="#000"/>
    <g stroke="#bdbdbd" stroke-width=".8">
      <line x1="145" y1="160" x2="145" y2="455"/>
      <line x1="283" y1="160" x2="283" y2="455"/>
      <line x1="428" y1="160" x2="428" y2="455"/>
      <line x1="574" y1="160" x2="574" y2="455"/>
      <line x1="0" y1="160" x2="600" y2="160"/>
      <line x1="0" y1="455" x2="600" y2="455"/>
    </g>
    <!-- bottom flaps -->
    <path d="M0,457 H145 V603 Q145,615 133,615 H12 Q0,615 0,603 Z" fill="#fff"/>
    <line x1="0" y1="595" x2="145" y2="595" stroke="#bdbdbd" stroke-width=".8"/>
    <path d="M145,455 L162,505 Q168,520 185,520 H243 Q260,520 266,505 L283,455 Z" fill="#fff"/>
    <path d="M428,455 L445,505 Q451,520 468,520 H534 Q551,520 557,505 L574,455 Z" fill="#fff"/>
  </svg>

  <p class="label flap-name">Fjellbrook Botanics</p>

  <h1 class="label brand-name">Fjellbrook<br>Botanics</h1>
  <p class="label product-name">Charcoal Activated<br>Face Mask</p>
  <div class="glow-swoosh" role="img" aria-label="Soft pink and blue swoosh of colour behind the tagline"></div>
  <p class="label tagline">restores your youthful glow</p>
  <p class="label volume">330ML</p>

  <p class="label back-mark">Fjellbrook Botanics</p>
  <p class="label ingredients">Ingredients: water, polyvinyl alcohol, glycerin, activated charcoal powder, kaolin, aloe leaf juice, butylene glycol, xanthan gum, panthenol, tea tree oil, phenoxyethanol, ethylhexylglycerin, citric acid, fragrance.</p>
  <p class="label certification">ISO901 &amp; GMPC CERTIFIED</p>
  <p class="label unisex-mark">FBUnisex</p>

  <p class="label front-mark">Fjellbrook<br>Botanics</p>
</main>
</body>
</html>
```